Medical Marijuana Service in the Bay Area

This is for a business card design that is going to be making medical marijuana deliveries in the bay area. The name of the the business is "Coastal Sage Wellness". I would like to have a modern feel and showing us as a medical marijuana company but at the same time discrete about it. I'm trying to target more sophisticated clients.

Industry/Entity Type

Medical

Contact Information for Business Card

Would like people to know it is for medical marijuana but in a discrete way.

```html
<!DOCTYPE html>
<html lang="en">
<head>
<meta charset="utf-8">
<title>Coastal Sage Wellness – Business Cards</title>
<link rel="stylesheet" href="https://fonts.googleapis.com/css2?family=Play:wght@400;700&display=swap">
<style>
  :root {
    --bg: #e9e6e1;
    --card: #ffffff;
    --lime: #8dc21f;
    --lime-dark: #6fa012;
    --lime-light: #b5dc5a;
    --ink: #4a4a4a;
    --white: #ffffff;
  }
  * { box-sizing: border-box; margin: 0; padding: 0; }
  html, body { width: 1200px; height: 900px; overflow: hidden; }
  body {
    background: var(--bg);
    font-family: "Play", sans-serif;
    position: relative;
  }
  .card {
    position: absolute;
    width: 640px;
    height: 366px;
    background: var(--card);
    box-shadow: 0 12px 30px rgba(0,0,0,.18);
    overflow: hidden;
  }
  .card-back { left: 130px; top: 64px; }
  .card-front { left: 430px; top: 470px; }

  .card-back .wave { position: absolute; inset: 0; width: 100%; height: 100%; }
  .holder-name {
    position: absolute; left: 40px; top: 30px;
    font-size: 26px; font-weight: 700; color: var(--lime);
  }
  .back-brand {
    position: absolute; left: 70px; top: 200px;
    display: flex; flex-direction: column; align-items: center; gap: 10px;
  }
  .brand-dot { width: 38px; height: 38px; border-radius: 50%; }
  .back-brand .brand-dot { background: var(--white); }
  .back-brand .brand-name {
    color: var(--white); font-size: 26px; font-weight: 700; white-space: nowrap;
  }
  .divider {
    position: absolute; left: 372px; top: 160px; width: 1px; height: 150px;
    background: rgba(255,255,255,.7);
  }
  .contact-list {
    position: absolute; left: 392px; top: 166px; list-style: none;
    display: flex; flex-direction: column; gap: 13px;
  }
  .contact-list li {
    display: flex; align-items: center; gap: 12px;
    color: var(--white); font-size: 15px;
  }
  .contact-list svg { width: 18px; height: 18px; flex: none; }

  .front-brand {
    position: absolute; left: 0; right: 0; top: 118px;
    display: flex; flex-direction: column; align-items: center; gap: 22px;
  }
  .front-brand .brand-dot { background: var(--lime); width: 50px; height: 50px; }
  .front-brand .brand-name {
    color: var(--ink); font-size: 44px; font-weight: 400; white-space: nowrap;
  }
</style>
</head>
<body>
  <section class="card card-back">
    <svg class="wave" viewBox="0 0 640 366" preserveAspectRatio="none" aria-hidden="true">
      <path d="M0 96 C160 70 300 120 640 80 L640 366 L0 366 Z" fill="var(--lime-light)"/>
      <path d="M0 112 C170 86 320 138 640 98 L640 366 L0 366 Z" fill="var(--lime)"/>
      <path d="M0 112 C170 86 320 138 640 98 L640 118 C320 158 170 106 0 132 Z" fill="var(--lime-dark)" opacity=".55"/>
    </svg>
    <div class="holder-name">Daniel Reyes</div>
    <div class="back-brand">
      <span class="brand-dot"></span>
      <span class="brand-name">Coastal Sage Wellness</span>
    </div>
    <div class="divider"></div>
    <ul class="contact-list">
      <li>
        <svg viewBox="0 0 24 24"><path fill="#fff" d="M6.6 10.8a15 15 0 0 0 6.6 6.6l2.2-2.2c.3-.3.7-.4 1-.2 1.1.4 2.3.6 3.6.6.6 0 1 .4 1 1V20c0 .6-.4 1-1 1A17 17 0 0 1 3 4c0-.6.4-1 1-1h3.5c.6 0 1 .4 1 1 0 1.3.2 2.5.6 3.6.1.3 0 .7-.2 1z"/></svg>
        Tel: 415 555 0148
      </li>
      <li>
        <svg viewBox="0 0 24 24"><rect x="4" y="3" width="16" height="18" rx="2" fill="none" stroke="#fff" stroke-width="2"/><path d="M8 8h8M8 12h8M8 16h5" stroke="#fff" stroke-width="2"/></svg>
        Fax: 415 555 0192
      </li>
      <li>
        <svg viewBox="0 0 24 24"><rect x="3" y="5" width="18" height="14" rx="1" fill="none" stroke="#fff" stroke-width="2"/><path d="M3 6l9 7 9-7" fill="none" stroke="#fff" stroke-width="2"/></svg>
        hello@coastalsage.example
      </li>
      <li>
        <svg viewBox="0 0 24 24"><rect x="3" y="3" width="18" height="18" rx="2" fill="#fff"/></svg>
        Follow us online
      </li>
    </ul>
  </section>

  <section class="card card-front">
    <div class="front-brand">
      <span class="brand-dot"></span>
      <span class="brand-name">Coastal Sage Wellness</span>
    </div>
  </section>
</body>
</html>
```